Fornello Oak Hearth Kitchen (restaurant)

Restaurant with a cool vibe.
We need a refresh of existing site. Appealing to a hip crowd of 25 or older age bracket (mid price to high small town). Constant changes food and cocktail menu. A vibing atmosphere with jazz funk hip music.
Must be able to scale for any device… phone/mobile device super important.
Instagram: @Velmora.Brisket
Website: velmorabrisket.example

Target Market(s)

25-55 age group

Number of Pages Required

1 page

Font styles to use
Sans Serif

Requirements
Must have
• Simple to navigate. Simplicity is the key to all sophistication.

Links/Buttons
Menu
Gift Cards
Reservations
Take Out
Contact Us
Should not have
• Please, nothing generic looking… no cookie cutter look. Originality

```html
<!DOCTYPE html>
<html lang="en">
<head>
<meta charset="utf-8">
<title>Fornello Oak Hearth Kitchen</title>
<link href="https://fonts.googleapis.com/css2?family=Young+Serif&family=Lora:ital,wght@0,400;0,600;1,400&family=Outfit:wght@400;600;800&display=swap" rel="stylesheet">
<style>
:root{
  --orange:#f7931e;
  --brown:#b5725a;
  --dark:#0f2a31;
  --darker:#0b2027;
  --ink:#2b2b2b;
  --muted:#666;
  --light:#e9e7e7;
  --white:#fff;
}
*{margin:0;padding:0;box-sizing:border-box}
html,body{width:1200px;height:5358px;overflow:hidden}
body{font-family:"Lora",serif;color:var(--ink);background:var(--white);position:relative}
section,header,footer{position:relative;width:1200px;overflow:hidden}
.abs{position:absolute}
.display{font-family:"Young Serif",serif;font-weight:400}
.img{position:absolute;display:block}

/* header */
.site-header{height:108px;background:var(--white)}
.brand{left:173px;top:30px;color:var(--brown);font-family:"Outfit",sans-serif}
.brand-name{font-size:28px;font-weight:800;letter-spacing:1px;line-height:30px}
.brand-tag{font-size:12px;margin-left:20px;line-height:14px}
.nav{left:0;top:46px;font-size:15px}
.nav a{position:absolute;white-space:nowrap;color:var(--ink);text-decoration:none}
.btn{display:inline-block;text-align:center;font-size:15px;font-weight:600;color:var(--white);text-decoration:none}
.btn-orange{background:var(--orange)}
.btn-outline{border:2px solid var(--white)}

/* hero */
.hero{height:570px;background:linear-gradient(100deg,#3a2c22 0%,#5a4434 40%,#2d2620 70%,#4b3a2c 100%)}
.hero-title-small{left:154px;top:168px;font-size:40px;line-height:44px;color:var(--white)}
.hero-title{left:154px;top:218px;font-size:76px;color:var(--white);line-height:1}
.social-col{left:1026px;top:68px;display:flex;flex-direction:column;gap:12px}
.dot{width:12px;height:12px;border-radius:50%;background:var(--white)}
.slider-bar{top:510px;height:3px;width:44px}

/* welcome */
.welcome{height:566px}
.eyebrow{font-family:"Outfit",sans-serif;font-size:17px}
.copy{font-size:15px;line-height:26px;color:var(--muted)}

/* menu */
.special{height:805px;background:var(--dark)}
.section-title{width:100%;text-align:center;font-size:60px}
.dish{width:200px;height:200px;border-radius:50%;border:5px solid var(--white)}
.dish-label{width:240px;text-align:center;color:var(--white);font-size:28px;line-height:30px}

/* why */
.why{height:366px;background:linear-gradient(90deg,#1b3138 0%,#26383d 40%,#12262d 100%)}
.feature{width:264px;height:228px;background:var(--white);padding:20px}
.feature h3{font-family:"Young Serif",serif;font-weight:400;font-size:24px;margin-top:18px}
.feature p{font-size:14px;line-height:22px;color:var(--muted);margin-top:8px}
.feature-icon{width:38px;height:46px}

/* hours */
.hours{height:666px}
.hours h4{font-size:22px;font-weight:600;color:var(--ink)}
.hours p{font-size:16px;line-height:29px;color:var(--muted)}

/* subscribe */
.subscribe{height:202px;background:linear-gradient(90deg,#0e252c,#1d343a 50%,#0e252c)}
.field{left:460px;top:79px;width:430px;height:56px;background:var(--white);font-size:14px;color:#555;padding:20px 16px}
.field-btn{left:890px;top:79px;width:154px;height:56px;line-height:56px}

/* gift */
.gift{height:609px}
/* testimonial */
.testimonial{height:416px;background:var(--light)}
.arrow{width:20px;height:36px}

/* footer */
.site-footer{height:416px;background:var(--darker);color:#cfd5d6}
.foot-head{font-family:"Young Serif",serif;font-size:19px;color:var(--white);line-height:24px}
.foot-text{font-size:14px;line-height:24px;color:#c7cdce}
</style>
</head>
<body>

<header class="site-header">
  <div class="abs brand">
    <div class="brand-name">FORNELLO</div>
    <div class="brand-tag">Oak Hearth Kitchen</div>
  </div>
  <nav class="abs nav">
    <a style="left:376px" href="#">Menu</a>
    <a style="left:451px" href="#">Gift Cards</a>
    <a style="left:557px" href="#">Reservations</a>
    <a style="left:684px" href="#">Take Out</a>
    <a style="left:782px" href="#">Contact Us</a>
  </nav>
  <a class="abs btn btn-orange" style="left:884px;top:33px;width:135px;height:42px;line-height:42px" href="#">Order Online</a>
</header>

<section class="hero">
  <div class="img" role="img" aria-label="Warm restaurant interior with wooden bar and counter seating" style="inset:0;background:radial-gradient(ellipse at 55% 30%,rgba(150,120,90,.5),transparent 60%)"></div>
  <div class="abs display hero-title-small">An Ambient Dining</div>
  <h1 class="abs display hero-title">Experience!</h1>
  <a class="abs btn btn-orange" style="left:160px;top:339px;width:160px;height:48px;line-height:48px" href="#">Book A Table</a>
  <a class="abs btn btn-outline" style="left:333px;top:339px;width:160px;height:48px;line-height:44px" href="#">Hours &amp; Contact</a>
  <div class="abs social-col"><span class="dot"></span><span class="dot"></span><span class="dot"></span><span class="dot"></span></div>
  <span class="abs slider-bar" style="left:158px;background:var(--orange)"></span>
  <span class="abs slider-bar" style="left:210px;background:rgba(255,255,255,.5)"></span>
  <span class="abs slider-bar" style="left:262px;background:rgba(255,255,255,.5)"></span>
</section>

<section class="welcome">
  <div class="img" role="img" aria-label="Wood fired pizza with arugula in front of the pizza oven" style="left:156px;top:73px;width:453px;height:435px;border-radius:0 0 70px 0;background:linear-gradient(160deg,#3b3a38 0%,#6b5a45 45%,#b8894f 75%,#7e9a4a 100%)"></div>
  <div class="img" role="img" aria-label="Bowl of dip seen from above" style="left:506px;top:92px;width:136px;height:136px;border-radius:50%;background:radial-gradient(circle,#a8b05a 0%,#6c7a35 55%,#2f2f2f 75%);border:4px solid #555"></div>
  <div class="img" role="img" aria-label="Bowl of soup seen from above" style="left:47px;top:340px;width:156px;height:156px;border-radius:50%;background:radial-gradient(circle,#c28a3e 0%,#8b5a24 55%,#707070 72%,#a0a0a0 100%)"></div>
  <div class="abs eyebrow" style="left:686px;top:102px">Welcome to</div>
  <h2 class="abs display" style="left:686px;top:124px;font-size:56px;color:var(--brown)">Fornello</h2>
  <p class="abs copy" style="left:686px;top:194px;width:360px">Lorem ipsum dolor sit amet, consectetur adipiscing elit. Proin pharetra nibh sem, eget egestas ligula interdum non. Proin eu risus nisl. Suspendisse quis erat vitae elit ultricies imperdiet id nec felis. Sed turpis libro, rhoncus sit amet leo non, condimentum lobortis sem. Fusce eu felis sapien. Pellentesque habitant morbi tristue senectus et netus et malesuada famturpis egestas. Morbi consequat vehicula dui at mattis.</p>
</section>

<section class="special">
  <h2 class="abs display section-title" style="top:50px;color:var(--white)">Special Menu</h2>
  <div class="img dish" role="img" aria-label="Burger" style="left:156px;top:150px;background:radial-gradient(circle,#8a5a30,#c89a5a 60%,#6b3a20)"></div>
  <div class="img dish" role="img" aria-label="Sandwiches" style="left:385px;top:150px;background:radial-gradient(circle,#e8d49a,#b8955a 60%,#5a6a3a)"></div>
  <div class="img dish" role="img" aria-label="Wood fired pizza" style="left:613px;top:150px;background:radial-gradient(circle,#d8a060,#a8502a 60%,#6a6a5a)"></div>
  <div class="img dish" role="img" aria-label="Mains and pasta" style="left:842px;top:150px;background:radial-gradient(circle,#d8c8b8,#8a5a4a 60%,#4a4a4a)"></div>
  <div class="abs dish-label display" style="left:136px;top:356px">Burgers</div>
  <div class="abs dish-label display" style="left:365px;top:356px">Sandwiches</div>
  <div class="abs dish-label display" style="left:593px;top:356px">Wood Fired<br>Pizza</div>
  <div class="abs dish-label display" style="left:822px;top:356px">Mains &amp; Pasta</div>
  <div class="img dish" role="img" aria-label="Shareable tacos" style="left:156px;top:455px;background:radial-gradient(circle,#c86a8a,#6a3a5a 55%,#d8c090)"></div>
  <div class="img dish" role="img" aria-label="Salad" style="left:385px;top:455px;background:radial-gradient(circle,#9ac85a,#4a7a2a 50%,#0a0a0a 80%)"></div>
  <div class="img dish" role="img" aria-label="Pizza" style="left:613px;top:455px;background:radial-gradient(circle,#c8503a,#a8683a 60%,#3a3a3a)"></div>
  <div class="img dish" role="img" aria-label="Other dishes" style="left:842px;top:455px;background:radial-gradient(circle,#c8a05a,#7a8a4a 60%,#3a3a3a)"></div>
  <div class="abs dish-label display" style="left:136px;top:661px">Shareables</div>
  <div class="abs dish-label display" style="left:365px;top:661px">Salads</div>
  <div class="abs dish-label display" style="left:593px;top:661px">Pizza</div>
  <div class="abs dish-label display" style="left:822px;top:661px">Other</div>
</section>

<section class="takeout" style="height:634px">
  <h2 class="abs display" style="left:154px;top:128px;font-size:64px;color:var(--brown)">Take Out</h2>
  <p class="abs copy" style="left:154px;top:212px;width:380px">Proin eu risus nisl. Suspendisse quis erat vitae elit ultricies imperdiet id nec felis. Sed turpis libro, rhoncus sit amet leo non, condimentum lobortis sem. Fusce eu felis sapien. Pellentesque habitant morbi tristue senectus et netus et malesuada famturpis egestas. Morbi consequat vehicula dui at mattis.</p>
  <div class="abs" style="left:154px;top:410px;font-size:20px">Call us for order</div>
  <div class="abs display" style="left:154px;top:442px;font-size:44px;color:var(--orange)">555-214-0388</div>
  <div class="img" role="img" aria-label="Friends laughing while sharing pizza" style="left:589px;top:91px;width:453px;height:435px;border-radius:70px 0 70px 0;background:linear-gradient(135deg,#8a7a6a 0%,#b89478 40%,#8a3a3a 70%,#5a4a3a 100%)"></div>
</section>

<section class="why">
  <div class="img" role="img" aria-label="Smiling guests in the dining room, darkened" style="inset:0;background:radial-gradient(ellipse at 25% 50%,rgba(120,100,80,.25),transparent 60%)"></div>
  <div class="abs eyebrow" style="left:156px;top:128px;color:var(--white)">Why people</div>
  <h2 class="abs display" style="left:156px;top:150px;font-size:58px;color:var(--white)">Choose us?</h2>
  <div class="abs feature" style="left:489px;top:63px">
    <svg class="feature-icon" viewBox="0 0 38 46"><rect x="0" y="0" width="38" height="46" fill="#f7931e"/><rect x="8" y="10" width="22" height="3" fill="#fff"/><rect x="8" y="18" width="22" height="2" fill="#fff"/><rect x="8" y="24" width="16" height="2" fill="#fff"/></svg>
    <h3>Explore the menu</h3>
    <p>Fusce eu felen. Pellentesque habitant mbi tristue senectus et netus et malada famturpis egestas.</p>
  </div>
  <div class="abs feature" style="left:776px;top:63px">
    <svg class="feature-icon" viewBox="0 0 60 46" style="width:60px"><rect x="2" y="10" width="34" height="24" fill="#d9533a"/><path d="M36 18h12l8 8v8H36z" fill="#3b4a6a"/><circle cx="14" cy="38" r="5" fill="#333"/><circle cx="46" cy="38" r="5" fill="#333"/></svg>
    <h3>We Deliver</h3>
    <p>Fusce eu felen. Pellentesque habitant mbi tristue senectus et netus et malada famturpis egestas.</p>
  </div>
</section>

<section class="hours">
  <h2 class="abs display section-title" style="top:38px;color:var(--brown);font-size:62px">Working Hour</h2>
  <h4 class="abs" style="left:154px;top:216px">Dining Hours</h4>
  <p class="abs" style="left:154px;top:257px">Courtyard is open<br>Thursday to Sunday<br>12:00pm – 9:00pm</p>
  <h4 class="abs" style="left:154px;top:368px">Pickup &amp; Kitchen Hours</h4>
  <p class="abs" style="left:154px;top:409px">Thursday to Sunday<br>12:00pm – 8:00pm</p>
  <div class="img" role="img" aria-label="Colourful courtyard patio with umbrellas" style="left:535px;top:150px;width:364px;height:437px;border-radius:70px 0 70px 0;background:linear-gradient(160deg,#c0502a 0%,#e2783a 30%,#3a8ac0 55%,#c8402a 75%,#6a4a3a 100%)"></div>
  <div class="img" role="img" aria-label="Smiling guest with a plate of food" style="left:809px;top:279px;width:233px;height:233px;border-radius:70px 0 0 0;background:linear-gradient(150deg,#b8563a 0%,#d8a078 45%,#e8c078 80%,#d88a3a 100%)"></div>
  <div class="img" role="img" aria-label="Pizza seen from above" style="left:441px;top:410px;width:137px;height:135px;background:radial-gradient(circle,#d8603a,#e8c090 60%,#5a3a6a 80%)"></div>
</section>

<section class="subscribe">
  <div class="abs eyebrow" style="left:156px;top:71px;color:var(--white)">Newsletter</div>
  <h2 class="abs display" style="left:156px;top:96px;font-size:58px;color:var(--white)">Subscribe</h2>
  <div class="abs field">Enter Email Address</div>
  <a class="abs btn btn-orange field-btn" href="#">Subscribe</a>
</section>

<section class="gift">
  <div class="img" role="img" aria-label="Hand holding a gift card in a warmly lit restaurant" style="left:156px;top:91px;width:483px;height:435px;border-radius:0 70px 0 70px;background:linear-gradient(135deg,#c8b8a8 0%,#8a5a3a 45%,#3a2418 75%,#b87a4a 100%)"></div>
  <div class="img" role="img" aria-label="Red gift card with a gold bow" style="left:474px;top:199px;width:248px;height:156px;background:linear-gradient(135deg,#d8252a,#a81418)"></div>
  <h2 class="abs display" style="left:751px;top:188px;font-size:96px;line-height:100px;color:var(--brown)">Gift<br>Cards</h2>
  <div class="abs" style="left:751px;top:395px;font-size:21px;color:var(--muted)">Fusce felis turpis, maximus</div>
</section>

<section class="testimonial">
  <div class="img" role="img" aria-label="Pizza seen from above" style="left:-110px;top:-120px;width:330px;height:286px;border-radius:50%;background:radial-gradient(circle,#e8c08a,#c87a4a 70%,#8a5a3a)"></div>
  <div class="img" role="img" aria-label="Plated salad seen from above" style="left:1024px;top:240px;width:260px;height:260px;border-radius:50%;background:radial-gradient(circle,#d8a05a,#7a8a3a 55%,#4a4a4a 75%)"></div>
  <svg class="abs" style="left:558px;top:52px" width="92" height="64" viewBox="0 0 92 64"><path d="M20 64a20 20 0 1 1 18-28c4 14-2 28-18 28zM8 30C8 12 20 2 34 0v6C22 8 16 16 16 24z" fill="#c08a78"/><path d="M70 64a20 20 0 1 1 18-28c4 14-2 28-18 28zM58 30C58 12 70 2 84 0v6C72 8 66 16 66 24z" fill="#c08a78"/></svg>
  <div class="abs" style="width:100%;top:150px;text-align:center;font-size:20px;color:var(--brown)">My favorite Fornello oak hearth kitchen</div>
  <p class="abs" style="left:240px;top:196px;width:720px;text-align:center;font-style:italic;font-size:16px;line-height:33px;color:var(--muted)">Lorem ipsum dolor sit amet, consectetur adipiscing elit. Mauris quam nibh, pharetra eget tincidunt a, congue id tellus. Maecenas eget metus lacinia, malesuada eros eget, dapibus nulla. Donec ex sem, malesuada quis faucibus.</p>
  <div class="abs" style="width:100%;top:306px;text-align:center;font-size:19px;font-weight:600">Lorem ipsum</div>
  <div class="abs" style="width:100%;top:336px;text-align:center;font-size:13px;font-style:italic;color:#999">Simply Dummy</div>
  <svg class="abs arrow" style="left:156px;top:206px" viewBox="0 0 20 36"><path d="M18 2L2 18l16 16" stroke="#333" stroke-width="2" fill="none"/></svg>
  <svg class="abs arrow" style="left:1024px;top:206px" viewBox="0 0 20 36"><path d="M2 2l16 16L2 34" stroke="#333" stroke-width="2" fill="none"/></svg>
</section>

<footer class="site-footer">
  <div class="abs brand" style="left:156px;top:44px;color:var(--white)">
    <div class="brand-name">FORNELLO</div>
    <div class="brand-tag">Oak Hearth Kitchen</div>
  </div>
  <div class="abs" style="left:926px;top:58px;display:flex;gap:18px"><span class="dot"></span><span class="dot"></span><span class="dot"></span><span class="dot"></span></div>
  <div class="abs" style="left:154px;top:119px;width:888px;border-top:2px dotted #6a7a7e"></div>
  <div class="abs foot-head" style="left:154px;top:152px">Contact Info</div>
  <div class="abs foot-text" style="left:154px;top:188px">
    <div style="display:flex;gap:10px"><svg width="12" height="16" viewBox="0 0 12 16" style="margin-top:4px"><path d="M6 0a6 6 0 0 1 6 6c0 4-6 10-6 10S0 10 0 6a6 6 0 0 1 6-6z" fill="#fff"/><circle cx="6" cy="6" r="2" fill="#0b2027"/></svg><span>48 Larkspur Row<br>Brindlewood, ON</span></div>
    <div style="display:flex;gap:10px;margin-top:10px"><svg width="12" height="14" viewBox="0 0 12 14" style="margin-top:5px"><path d="M2 0h3l1 4-2 1c1 2 2 3 4 4l1-2 3 1v3c0 1-1 2-2 2C4 13-1 8 0 2c0-1 1-2 2-2z" fill="#fff"/></svg><span>555-214-0388</span></div>
    <div style="display:flex;gap:10px;margin-top:10px"><svg width="14" height="11" viewBox="0 0 14 11" style="margin-top:7px"><rect width="14" height="11" fill="#fff"/><path d="M0 0l7 6 7-6" stroke="#0b2027" fill="none"/></svg><span>hello@velmorabrisket.example</span></div>
  </div>
  <div class="abs foot-head" style="left:403px;top:148px">Dining Hours</div>
  <div class="abs foot-text" style="left:403px;top:188px">Courtyard is open<br>Thursday to Sunday<br>12:00pm – 9:00pm</div>
  <div class="abs foot-head" style="left:611px;top:148px;width:200px">Pickup &amp; Kitchen<br>Hours</div>
  <div class="abs foot-text" style="left:611px;top:212px">Thursday to Sunday<br>12:00pm – 8:00pm</div>
  <div class="abs foot-head" style="left:857px;top:148px">Reservations</div>
  <div class="abs foot-text" style="left:857px;top:188px;width:190px">Reservations will not be available for the courtyard Under phase 1 and 2 of reopening. Walk-ins only. We can't wait to see you!</div>
  <div class="abs foot-text" style="left:154px;top:360px;font-size:13px">© 2021 <strong>Fornello oak hearth kitchen</strong>. All right reserved</div>
  <a class="abs" style="right:158px;top:362px;font-size:12px;font-weight:600;color:var(--orange);text-decoration:none" href="#">BACK TO TOP</a>
</footer>

</body>
</html>
```